Mastering the Art of Challenging Conversations

I need a professional powerpoint presentation to use when teaching corporate workshops about how to handle hard conversations. I want it to be colorful, but not cartoonish. The images I attached are from corvina stock photos - I like the colors and the look of the image with the people and the conversation and thought "bubbles" above their heads. I also like the image of the two conversation bubbles with heads inside the bubbles. The slides will not have a lot of text on them so the design will be prominent. I'm also open to the idea of stock photos showing people engaged in both frustrating and successful conversations.

Target Market(s)

Corporate Managers

Industry/Entity Type

Corporate Talent Development

Font styles to use
Sans Serif

Colors
0094D4
00A9DD
6FCCEA
C7EBF8
E9F6FB
F0912C
F2A743
F7CA91
FBE8D2
FDF5EE
6B429C
8869AF
B7A5CE
E3DAEB
F3F0F8

Requirements
Must have
• An uncluttered look - professional, but not stuffy. Colorful but not cartoonish,
Nice to have
• The presentation is all about how to have conversations. So conversation and thought bubbles should be used in the design but not overdone.
Should not have
• cartoons, clip art, patterns (only solid colors for fill in and backgrounds)

```html
<!DOCTYPE html>
<html lang="en">
<head>
<meta charset="utf-8">
<title>Challenging Conversations – Dialogue Slide</title>
<link rel="stylesheet" href="https://fonts.googleapis.com/css2?family=Carlito:wght@400&display=swap">
<style>
  :root {
    --violet: #6B429C;
    --violet-text: #74479B;
    --orange: #F0822F;
    --orange-text: #EE7F3A;
    --bubble: #FFFFFF;
    --mid-rose: #C0676F;
  }
  * { margin: 0; padding: 0; box-sizing: border-box; }
  html, body {
    width: 1200px;
    height: 675px;
    overflow: hidden;
  }
  .slide {
    position: relative;
    width: 1200px;
    height: 675px;
    background: linear-gradient(90deg, var(--violet) 0%, #7C4B98 18%, var(--mid-rose) 52%, #E27A49 78%, var(--orange) 100%);
    font-family: "Carlito", "Calibri", sans-serif;
    overflow: hidden;
  }
  .dialogue-art {
    position: absolute;
    inset: 0;
    width: 1200px;
    height: 675px;
  }
  .bubble-shape { fill: var(--bubble); }
  .speaker-left { fill: var(--violet-text); }
  .speaker-right { fill: var(--orange-text); }
  .bubble-text {
    position: absolute;
    top: 258px;
    font-size: 21.5px;
    line-height: 27px;
    letter-spacing: 0.1px;
  }
  .bubble-text--left {
    left: 309px;
    color: var(--violet-text);
    text-align: left;
  }
  .bubble-text--right {
    right: calc(1200px - 864px);
    color: var(--orange-text);
    text-align: right;
  }
</style>
</head>
<body>
<main class="slide">
  <svg class="dialogue-art" viewBox="0 0 1200 675" xmlns="http://www.w3.org/2000/svg">
    <defs>
      <clipPath id="bubble-left-clip">
        <path d="M144.5 188 H289.7 L358.7 211 L427.1 188 H452.6 A77 77 0 0 1 529.6 265 V572.8 A77 77 0 0 1 452.6 649.8 H144.5 A77 77 0 0 1 67.5 572.8 V265 A77 77 0 0 1 144.5 188 Z"/>
      </clipPath>
      <clipPath id="bubble-right-clip">
        <path d="M730.8 188 L797.5 211 L865.5 188 H1043.3 A77 77 0 0 1 1120.3 265 V572.8 A77 77 0 0 1 1043.3 649.8 H741.7 A77 77 0 0 1 664.7 572.8 V265 A66 77 0 0 1 730.8 188 Z"/>
      </clipPath>
    </defs>

    <g class="bubble bubble--left">
      <path class="bubble-shape" d="M144.5 188 H289.7 L358.7 211 L427.1 188 H452.6 A77 77 0 0 1 529.6 265 V572.8 A77 77 0 0 1 452.6 649.8 H144.5 A77 77 0 0 1 67.5 572.8 V265 A77 77 0 0 1 144.5 188 Z"/>
      <rect class="speaker-left" clip-path="url(#bubble-left-clip)" x="60" y="224" width="216" height="393" rx="60"
            role="img" aria-label="Purple silhouette of a person in profile, facing right"/>
    </g>

    <g class="bubble bubble--right">
      <path class="bubble-shape" d="M730.8 188 L797.5 211 L865.5 188 H1043.3 A77 77 0 0 1 1120.3 265 V572.8 A77 77 0 0 1 1043.3 649.8 H741.7 A77 77 0 0 1 664.7 572.8 V265 A66 77 0 0 1 730.8 188 Z"/>
      <rect class="speaker-right" clip-path="url(#bubble-right-clip)" x="897" y="232" width="230" height="383" rx="60"
            role="img" aria-label="Orange silhouette of a person in profile, facing left"/>
    </g>
  </svg>

  <p class="bubble-text bubble-text--left">
    Lorem ipsum dolor<br>sit amet,<br>consectetur<br>adipiscing elit, sed<br>do eiusmod tempor<br>incididunt ut labore<br>et dolore magna<br>aliqua.
  </p>

  <p class="bubble-text bubble-text--right">
    Lorem ipsum dolor<br>sit amet,<br>consectetur<br>adipiscing elit, sed<br>do eiusmod tempor<br>incididunt ut labore<br>et dolore magna<br>aliqua.
  </p>
</main>
</body>
</html>
```